Re-design a website for a millionaire mentor

We need an expert website designer to re-design the website vKeenstride.net

The website would have 4 pages. A home page, Summit Circle page, Hire RM page and an About page.

Here are some reference websites

https://www.lumovance.net
https://rolfbanter.net/

I will also attach a beginning of mockup of the home page I did myself to give an idea of the style we like, please use the quote "If you are not chasing your potential you are wasting your life" instead of the one in the current website...

You don't have the use the mockup (just the quote) and are free to use all your creativity.

Target Market(s)

Entrepreneurs

Number of Pages Required

4 page

Font styles to use
Other font styles liked:
• Franklin Gothic

Requirements
Must have
• -Call of action on the main page to download a free business plan
• -Hire rm page check out reference: http://www.hiremarkbellow.net
• -summit circle page with a button to sign in or join the summit circle. Check out reference for example: https://www.lumovance.net/glide_academy

```html
<!DOCTYPE html>
<html lang="en">
<head>
<meta charset="utf-8">
<title>vKeenstride — Home</title>
<link rel="stylesheet" href="https://fonts.googleapis.com/css2?family=Libre+Franklin:wght@400;500;600;800;900&family=Source+Sans+3:ital,wght@0,300;0,400;0,600;0,700;1,700;1,800&display=swap">
<style>
  :root {
    --red: #ee3a33;
    --yellow: #ffcc00;
    --ink: #111111;
    --night: #05070d;
    --white: #ffffff;
    --sky-top: #e3f3fa;
    --sky-bottom: #f4fbfd;
    --muted: #c9ccd4;
  }
  * { box-sizing: border-box; margin: 0; padding: 0; }
  html, body { width: 1200px; height: 1200px; overflow: hidden; }
  body {
    position: relative;
    background: var(--white);
    font-family: "Source Sans 3", sans-serif;
    color: var(--ink);
  }

  /* Header */
  .brand {
    position: absolute; left: 176px; top: 44px;
    display: flex; align-items: center; gap: 10px;
    font-family: "Source Sans 3", sans-serif;
    font-weight: 700; font-size: 30px; color: var(--ink);
    letter-spacing: -0.5px;
  }
  .brand-mark { width: 18px; height: 18px; background: var(--red); }
  .main-nav {
    position: absolute; top: 20px; left: 728px;
    display: flex; gap: 32px;
    font-family: "Source Sans 3", sans-serif; font-size: 12.5px;
    text-transform: uppercase; color: var(--ink);
  }
  .main-nav a { color: inherit; text-decoration: none; position: relative; }
  .main-nav a.is-active { font-weight: 700; }
  .main-nav a.is-active::after {
    content: ""; position: absolute; left: 50%; top: 21px;
    width: 5px; height: 5px; margin-left: -2.5px;
    border-radius: 50%; background: var(--red);
  }

  /* Hero */
  .hero-bg { position: absolute; left: 0; top: 0; width: 1200px; height: 651px; }
  .hero-photo {
    position: absolute; left: 500px; top: 85px; width: 600px; height: 565px;
    background: radial-gradient(ellipse 45% 55% at 58% 45%, #4a5574 0%, #2a3149 40%, rgba(5,7,13,0) 80%);
  }
  .quote-frame {
    position: absolute; left: 133px; top: 157px; width: 489px; height: 225px;
    border: 6px solid var(--red);
  }
  .quote-text {
    position: absolute; left: 170px; top: 190px; width: 440px;
    font-family: "Source Sans 3", sans-serif; font-style: italic; font-weight: 700;
    font-size: 38px; line-height: 51px; letter-spacing: -1.4px; color: var(--white);
  }
  .quote-author {
    position: absolute; left: 380px; top: 393px; width: 132px; text-align: right;
    font-size: 12px; color: var(--muted);
  }
  .hero-rule { position: absolute; left: 162px; top: 429px; width: 334px; height: 1px; background: #3a3d46; }
  .hero-lead {
    position: absolute; left: 176px; top: 459px; width: 340px;
    font-size: 14px; line-height: 26px; color: var(--white);
  }
  .hero-lead strong { font-size: 17px; font-weight: 600; }
  .btn {
    position: absolute; top: 542px; height: 52px; border-radius: 26px;
    display: flex; align-items: center; justify-content: center; gap: 14px;
    font-family: "Source Sans 3", sans-serif; font-weight: 700; font-size: 19px;
    text-transform: uppercase; text-decoration: none;
  }
  .btn-sign-in { left: 144px; width: 156px; background: var(--red); color: var(--white); }
  .btn-premium {
    left: 328px; width: 238px; background: var(--yellow); color: var(--ink);
    box-shadow: 0 0 14px rgba(255, 204, 0, 0.45);
  }
  .vip-tag {
    border: 1.3px solid var(--ink); border-radius: 3px;
    font-size: 9px; font-weight: 600; padding: 1px 4px; letter-spacing: 1px;
  }

  /* Intro */
  .intro {
    position: absolute; left: 0; top: 651px; width: 1200px; height: 549px;
    background: linear-gradient(180deg, var(--sky-top), var(--sky-bottom));
    overflow: hidden;
  }
  .intro-photo {
    position: absolute; left: 64px; top: 52px; width: 406px; height: 500px;
    border-radius: 140px 140px 0 0;
    background: linear-gradient(180deg, #a47a62 0%, #6b4c3f 30%, #f2f2f2 50%, #1c1f2a 70%, #1c1f2a 100%);
    opacity: 0.9;
  }
  .intro-title {
    position: absolute; left: 540px; top: 62px;
    font-family: "Libre Franklin", sans-serif; line-height: 1;
  }
  .intro-title .accent {
    display: block; color: var(--red); font-weight: 900;
    font-size: 72px; letter-spacing: -2.5px;
  }
  .intro-title .line {
    display: block; font-weight: 400; font-size: 56px; margin-top: 12px; letter-spacing: -0.5px;
  }
  .intro-title .line b { font-weight: 800; letter-spacing: 2px; }
  .intro-title .line-last { letter-spacing: -2.5px; font-size: 58px; margin-top: 14px; }
  .intro-title .line-last b { letter-spacing: -2px; }
  .intro-copy {
    position: absolute; left: 539px; top: 335px; width: 473px;
    font-size: 19px; font-weight: 300; line-height: 33px;
    text-align: justify; hyphens: auto; color: var(--ink);
  }
  .intro-copy b { font-weight: 700; letter-spacing: 0.8px; }
</style>
</head>
<body>
  <svg class="hero-bg" viewBox="0 0 1200 651" aria-hidden="true">
    <polygon points="0,157 1200,44 1200,651 0,651" fill="var(--night)"/>
  </svg>

  <header>
    <div class="brand"><span class="brand-mark"></span>vKeenstride</div>
    <nav class="main-nav">
      <a href="#" class="is-active">Home</a>
      <a href="#">Summit Circle</a>
      <a href="#">Hire RM</a>
      <a href="#">About</a>
    </nav>
  </header>

  <section class="hero">
    <div class="hero-photo" role="img" aria-label="Mentor speaking on stage with a microphone, in blue-toned low light"></div>
    <div class="quote-frame"></div>
    <p class="quote-text">If you are not chasing your potential you are wasting your life</p>
    <p class="quote-author">Dale Morrow</p>
    <div class="hero-rule"></div>
    <p class="hero-lead"><strong>You can</strong> Sign In Today or get Premium access now with benefits.</p>
    <a href="#" class="btn btn-sign-in">Sign In
      <svg width="22" height="18" viewBox="0 0 22 18" aria-hidden="true"><path d="M1 9h19M12 1l8 8-8 8" fill="none" stroke="currentColor" stroke-width="2.2" stroke-linecap="round" stroke-linejoin="round"/></svg>
    </a>
    <a href="#" class="btn btn-premium"><span class="vip-tag">VIP</span>Premium Access</a>
  </section>

  <section class="intro">
    <div class="intro-photo" role="img" aria-label="Portrait of the mentor in a dark suit and white shirt against a pale sky"></div>
    <h1 class="intro-title">
      <span class="accent">MAKE MONEY</span>
      <span class="line">BY <b>MONETIZING</b></span>
      <span class="line line-last">YOUR <b>PASSIONS!</b></span>
    </h1>
    <p class="intro-copy"><b>THE ANSWER FOR ENTREPRENEURS</b>, delivering <b>VISION</b>, <b>CLARITY</b> and <b>CREATIVE SOLUTIONS</b> to business ideas that have lost their sense of direction. vKeenstride is the pit stop, having the ability to redefine purpose and give new life to an existing set of skills. The objective is to inspire business leaders to take off, confident at full speed, with a new outlook on their business model and the road ahead.</p>
  </section>
</body>
</html>
```